Criação de Papelaria (6 itens) para Arquitetura
" Trata-se de uma empresa do ramo de arquitetura e urbanismo, formada por um casal de jovens arquitetos. Os serviços podem ser prestados presencialmente através do contato direto com o cliente ou ainda por meio da internet, onde a abordagem com o cliente se dá através das redes sociais. A empresa pretende ampliar sua atuação na internet através do marketing digital e para isto necessita transmitir com clareza valores como: credibilidade, contemporaneidade, versatilidade e objetividade. "

```html
<!DOCTYPE html>
<html lang="pt-BR">
<head>
<meta charset="UTF-8">
<title>Vertana — Papel Timbrado</title>
<link href="https://fonts.googleapis.com/css2?family=Montserrat:wght@400;600;700&display=swap" rel="stylesheet">
<style>
  :root {
    --backdrop: #d9dadc;
    --paper: #ffffff;
    --brand-orange: #e8561c;
    --ink-dark: #3a3a3c;
    --ink-muted: #6d6e71;
    --ink-faint: #b4b5b8;
    --deco-light: #f4f4f5;
    --deco-mid: #dedfe1;
  }
  * { margin: 0; padding: 0; box-sizing: border-box; }
  html, body {
    width: 1200px; height: 1200px; overflow: hidden;
    background: var(--backdrop);
    font-family: "Montserrat", sans-serif;
  }
  .letterhead {
    position: absolute; left: 204px; top: 40px;
    width: 792px; height: 1120px;
    background: var(--paper);
    box-shadow: 0 6px 24px rgba(0,0,0,0.12);
    overflow: hidden;
  }
  .brand {
    position: absolute; left: 56px; top: 58px;
    display: flex; align-items: center; gap: 10px;
  }
  .brand-dot {
    width: 26px; height: 26px; border-radius: 50%;
    background: var(--brand-orange);
  }
  .brand-text { display: flex; flex-direction: column; }
  .brand-name {
    font-weight: 700; font-size: 30px; letter-spacing: 2px;
    color: var(--ink-dark); line-height: 1;
  }
  .brand-tagline {
    font-weight: 400; font-size: 9px; letter-spacing: 1px;
    color: var(--ink-muted); margin-top: 4px;
  }
  .header-rule {
    position: absolute; left: 250px; right: 0; top: 96px;
    height: 3px; background: var(--brand-orange);
  }
  .header-rule-accent {
    position: absolute; left: 560px; right: 0; top: 89px;
    height: 2px; background: var(--ink-dark);
  }
  .side-graphic {
    position: absolute; left: 440px; top: 230px;
    width: 352px; height: 540px;
    background: linear-gradient(160deg, var(--deco-light) 0%, var(--deco-mid) 100%);
  }
  .contact-bar {
    position: absolute; left: 56px; right: 40px; top: 1006px;
    display: flex; justify-content: space-between; align-items: flex-start;
  }
  .contact-item {
    display: flex; align-items: flex-start; gap: 7px;
    font-size: 10.5px; color: var(--ink-dark); line-height: 1.35;
  }
  .contact-icon { width: 16px; height: 16px; flex-shrink: 0; }
  .web-address {
    position: absolute; left: 0; right: 0; top: 1082px;
    text-align: center; font-size: 9px; letter-spacing: 2px;
    color: var(--ink-faint);
  }
</style>
</head>
<body>
  <main class="letterhead">
    <header>
      <div class="brand">
        <span class="brand-dot"></span>
        <div class="brand-text">
          <span class="brand-name">VERTANA</span>
          <span class="brand-tagline">Arquitetos + Urbanistas</span>
        </div>
      </div>
      <div class="header-rule-accent"></div>
      <div class="header-rule"></div>
    </header>

    <div class="side-graphic" role="img" aria-label="Grafismo decorativo em tons de cinza claro"></div>

    <footer>
      <div class="contact-bar">
        <div class="contact-item">
          <svg class="contact-icon" viewBox="0 0 16 16" aria-hidden="true">
            <circle cx="8" cy="8" r="8" fill="var(--brand-orange)"/>
            <path d="M5.5 4.5 L7 4.5 L7.6 6.2 L6.8 7 Q7.6 8.6 9 9.3 L9.8 8.5 L11.5 9.1 L11.5 10.6 Q8 11 5.5 7.5 Q5 6 5.5 4.5 Z" fill="#fff"/>
          </svg>
          <span>(11) 90000-4321</span>
        </div>
        <div class="contact-item">
          <svg class="contact-icon" viewBox="0 0 16 16" aria-hidden="true">
            <circle cx="8" cy="8" r="8" fill="var(--brand-orange)"/>
            <rect x="4" y="5.2" width="8" height="5.6" fill="#fff"/>
            <path d="M4 5.2 L8 8.3 L12 5.2" fill="none" stroke="var(--brand-orange)" stroke-width="0.9"/>
          </svg>
          <span>contato@vertana.com.br</span>
        </div>
        <div class="contact-item">
          <svg class="contact-icon" viewBox="0 0 16 16" aria-hidden="true">
            <circle cx="8" cy="8" r="8" fill="var(--brand-orange)"/>
            <rect x="4" y="5.2" width="8" height="5.6" fill="#fff"/>
            <path d="M4 5.2 L8 8.3 L12 5.2" fill="none" stroke="var(--brand-orange)" stroke-width="0.9"/>
          </svg>
          <span>projetos@vertana.com.br</span>
        </div>
        <div class="contact-item">
          <svg class="contact-icon" viewBox="0 0 16 16" aria-hidden="true">
            <circle cx="8" cy="8" r="8" fill="var(--brand-orange)"/>
            <path d="M8 12.5 Q4.8 8.6 4.8 6.8 A3.2 3.2 0 0 1 11.2 6.8 Q11.2 8.6 8 12.5 Z" fill="#fff"/>
            <circle cx="8" cy="6.8" r="1.2" fill="var(--brand-orange)"/>
          </svg>
          <span>Rua das Acácias 45 Jardim Norte<br>Porto Claro/SP CEP</span>
        </div>
      </div>
      <p class="web-address">www.vertana.com.br</p>
    </footer>
  </main>
</body>
</html>
```